Letterhead - Pelvarosi Law Group

I receive a fantastic logo from you guys and I'd like to incorporate it into business cards and letterhead. I accidentally approved design No. 58027913 and contacted designer Tarveck, and Tarveck sent me the zip folder for Design No. 58027986, which I very much appreciate.
I'd like to order business cards and letterhead with Design No. 58027986 as soon as possible, but I want to make sure that you incorporate the correct design (attached). I'd also like to provide my information to add (address, phone number, email, fax) but I'm not quite sure how to do it.
The information that I would like on the business cards and letterhead is as follows:
Pelvarosi Law Group
Dorian K. Pelvarosi, Esq.
2741 Halvern Street, Suite 306
San Francisco, CA 94019
Office: (415) 738-0461
Fax: (415) 386-7710
dory@pelvarosilawgroup.com
Thanks in advance for any guidance.
Dory Pelvarosi
Pelvarosi Law Group
(415) 574-8839 (cell)

```html
<!DOCTYPE html>
<html lang="en">
<head>
<meta charset="utf-8">
<title>Pelvarosi Law Group – Business Cards</title>
<link href="https://fonts.googleapis.com/css2?family=Outfit:wght@300;400;500;600&display=swap" rel="stylesheet">
<style>
  :root {
    --backdrop: #0a87c9;
    --card-dark: #141414;
    --card-mid: #2a2826;
    --ink-white: #f4f4f4;
    --ink-soft: #d6d6d6;
    --accent-blue: #1f8fd0;
  }
  * { box-sizing: border-box; margin: 0; padding: 0; }
  html, body {
    width: 1200px;
    height: 800px;
    overflow: hidden;
  }
  body {
    background: var(--backdrop);
    font-family: "Outfit", sans-serif;
    color: var(--ink-white);
    position: relative;
  }
  .card {
    position: absolute;
    width: 520px;
    height: 297px;
    background: var(--card-dark);
    border-radius: 3px;
    overflow: hidden;
    box-shadow: 0 18px 40px rgba(0, 20, 60, 0.35);
  }
  .card-front { left: 50px; top: 252px; }
  .card-back  { left: 630px; top: 252px; }

  .card-pattern {
    position: absolute;
    inset: 0;
    background:
      radial-gradient(ellipse at 60% 30%, rgba(70, 66, 62, 0.55), transparent 65%),
      linear-gradient(160deg, var(--card-mid) 0%, var(--card-dark) 70%, #0d0d0d 100%);
  }
  .card-content { position: absolute; inset: 0; }

  /* front side */
  .holder {
    position: absolute;
    left: 36px;
    top: 38px;
  }
  .holder-name {
    font-size: 22px;
    font-weight: 600;
    letter-spacing: 0.2px;
  }
  .holder-mobile {
    font-size: 12px;
    font-weight: 300;
    color: var(--ink-soft);
    margin-top: 1px;
  }
  .label { color: var(--accent-blue); }

  .contact-lines {
    position: absolute;
    left: 36px;
    top: 170px;
    font-size: 12px;
    font-weight: 300;
    line-height: 1.3;
    color: var(--ink-soft);
  }
  .address-block {
    position: absolute;
    left: 36px;
    top: 224px;
    font-size: 12px;
    font-weight: 300;
    line-height: 1.3;
    color: var(--ink-soft);
  }

  .firm-mark {
    position: absolute;
    display: flex;
    align-items: center;
    gap: 8px;
    color: var(--ink-white);
    font-weight: 500;
    white-space: nowrap;
  }
  .firm-mark-dot {
    border-radius: 50%;
    background: var(--accent-blue);
    flex: none;
  }
  .card-front .firm-mark {
    right: 30px;
    bottom: 40px;
    font-size: 15px;
  }
  .card-front .firm-mark-dot { width: 10px; height: 10px; }

  /* back side */
  .card-back .card-content {
    display: flex;
    flex-direction: column;
    align-items: center;
    justify-content: center;
    gap: 22px;
  }
  .card-back .firm-mark {
    position: static;
    font-size: 26px;
  }
  .card-back .firm-mark-dot { width: 16px; height: 16px; }
  .tagline {
    font-size: 13px;
    font-weight: 300;
    color: var(--ink-soft);
    letter-spacing: 0.3px;
  }
</style>
</head>
<body>

  <section class="card card-front">
    <div class="card-pattern" role="img" aria-label="Subtle dark geometric star tile pattern"></div>
    <div class="card-content">
      <div class="holder">
        <p class="holder-name">Dory Pelvarosi</p>
        <p class="holder-mobile"><span class="label">M:</span> (415) 574-8839</p>
      </div>

      <div class="contact-lines">
        <p><span class="label">T :</span> (415) 738-0461</p>
        <p><span class="label">F :</span> (415) 386-7710</p>
        <p><span class="label">E :</span> dory@pelvarosilawgroup.com</p>
      </div>

      <address class="address-block" style="font-style: normal;">
        <p>Pelvarosi Law Group</p>
        <p>Dorian K. Pelvarosi, Esq.</p>
        <p>2741 Halvern Street, Suite 306</p>
        <p>San Francisco, CA 94019</p>
      </address>

      <div class="firm-mark">
        <span class="firm-mark-dot"></span>
        <span class="firm-mark-name">Pelvarosi Law Group</span>
      </div>
    </div>
  </section>

  <section class="card card-back">
    <div class="card-pattern" role="img" aria-label="Subtle dark geometric star tile pattern"></div>
    <div class="card-content">
      <div class="firm-mark">
        <span class="firm-mark-dot"></span>
        <span class="firm-mark-name">Pelvarosi Law Group</span>
      </div>
      <p class="tagline">Thanks in advance for any guidance.</p>
    </div>
  </section>

</body>
</html>
```